Brighter House Storage Scheme Email marketing campaign for Tamsel Energy

Design a visually engaging and professional marketing email to promote the upcoming National Cell Storage Grant to our existing solar clients, encouraging them to install a battery system now to maximise savings. email content example "Subject: ⚡ National Cell Storage Grant is Coming – Maximise Your Solar Savings

Body:
Hi [First Name],

Great news! With the federal election now decided, the National Household Cell Grant Initiative is officially on the way.

While the scheme hasn’t formally launched yet, it's guaranteed—and like the solar rebate before it, the subsidy reduces each year, so the earlier you install, the more you’ll save.

Crucially, the subsidy is only available once per household, so it makes sense to install a system that fully meets your home's battery needs right from the start.

Why add a battery to your existing solar system now?
✅ Store your excess solar energy instead of sending it back to the grid for low feed-in tariffs
✅ Use your stored solar power at night, when electricity prices are highest (typically 5–8pm)
✅ Slash your power bills and avoid rising time-of-use charges
✅ Protect your home from power outages
✅ Increase your self-sufficiency and long-term energy security

If you’ve already installed solar with us, now is the ideal time to complete your setup with a battery system designed to maximise your return—and take full advantage of this one-off federal subsidy.

Call us today or reply to this email to secure your spot and beat the rush.

Let your solar work smarter for your home,
The Tamsel Energy Team"

Target Market(s)

Content: We’ve provided the copy (see attached or below). The key points to emphasise in the design are: The urgency (subsidy winds down each year, limited to one per household). The benefits of installing a battery now, including energy savings, time-of-use charge avoidance, and self-sufficiency. Call to action: “Call us today or reply to this email to secure your spot and beat the rush.”

Industry/Entity Type

Renewable Energy

Colors
0054AA
0677BA
7BADD7
CADEEF
E8F1F8
EB3D1F
EC4F4E
F09395
F8D3D4
FCEDEE

Requirements
Must have
• Clean, modern, and trustworthy – aligned with Tamsel Energy branding. Bold headers and icons to make key points stand out. Include visual elements such as: A solar battery image Infographic or icon-style section showing key battery benefits (e.g. bill savings, backup power, self-consumption) Highlighted call-to-action button (“Secure My Battery Now” or “Beat the Rush”)
Nice to have
• I would like to have our company imagery (Tamsel Energy) alongside the battery brands we offer being Borvo, KWM, Velimar and QuintaPWR
Should not have
• Unsure

```html
<!DOCTYPE html>
<html lang="en">
<head>
<meta charset="utf-8">
<title>Tamsel Energy – National Cell Storage Grant</title>
<link href="https://fonts.googleapis.com/css2?family=Oswald:wght@500;600;700&family=Lato:wght@400;700;900&family=Kaushan+Script&family=Yellowtail&display=swap" rel="stylesheet">
<style>
:root{
  --red:#d3202e;
  --red-dark:#b51824;
  --navy:#2f3548;
  --ink:#1c1d22;
  --mist:#dfe3ec;
  --paper:#ffffff;
  --sun:#e9a04a;
}
*{margin:0;padding:0;box-sizing:border-box}
html,body{width:922px;height:1200px;overflow:hidden;background:var(--paper)}
.email{position:relative;width:922px;height:1200px;overflow:hidden;background:var(--paper);font-family:'Lato',sans-serif;color:var(--ink)}
.abs{position:absolute}

/* header */
.brand{left:26px;top:36px;display:flex;align-items:center;gap:14px}
.brand-square{width:62px;height:62px;background:var(--red)}
.brand-name{font-family:'Oswald',sans-serif;font-weight:600;font-size:40px;line-height:1;color:var(--navy);letter-spacing:1px;text-transform:uppercase;width:200px}
.brand-tag{left:26px;top:128px;font-size:14px;color:var(--navy);letter-spacing:.3px;text-transform:uppercase}
.brand-reg{left:26px;top:160px;font-size:14px;line-height:19px;color:var(--ink)}

.headline-band{left:0;top:0;width:922px;height:150px}
.headline{right:24px;top:18px;text-align:right;font-family:'Oswald',sans-serif;font-weight:700;color:#fff;font-size:49px;line-height:54px;text-transform:uppercase}
.headline-script{right:22px;top:120px;font-family:'Kaushan Script',cursive;font-size:42px;color:var(--red);transform:rotate(-6deg);text-shadow:0 0 4px #fff,0 0 4px #fff}

.hero-photo{left:0;top:0;width:922px;height:440px}

.web-bar{left:0;top:216px;height:40px;width:360px}
.web-text{left:24px;top:222px;font-size:21px;font-weight:700;color:#fff}
.hero-box{left:0;top:256px;width:440px;height:128px}
.hero-title{left:24px;top:266px;font-family:'Oswald',sans-serif;font-weight:700;color:#fff;font-size:43px;line-height:49px;text-transform:uppercase}
.greet-band{left:0;top:384px;width:480px;height:50px;background:var(--mist)}
.greet{left:24px;top:396px;font-size:21px;color:var(--ink)}

/* body copy */
.lead{left:22px;top:450px;width:880px;font-size:18.5px;line-height:24px;font-weight:700;font-style:italic}
.lead em{color:var(--red);font-style:italic}
.para{left:22px;top:512px;width:760px;font-size:15.3px;line-height:20px}

.why-bar{left:22px;top:583px;width:594px;height:33px}
.why-text{left:36px;top:589px;font-size:16.5px;font-weight:900;color:#fff;text-transform:uppercase}

.benefits{left:34px;top:650px;list-style:none}
.benefits li{display:flex;align-items:center;gap:16px;font-size:16.3px;line-height:24px}
.benefits li b{font-weight:900}
.bullet{width:20px;height:14px;flex:none}

.battery-photo{left:796px;top:558px;width:90px;height:242px}

.note{left:26px;top:776px;width:872px;height:48px;background:var(--mist);padding:5px 0 0 16px;font-size:15.3px;line-height:20px}

.cta-bar{left:22px;top:838px;width:876px;height:38px;background:var(--navy);color:#fff;font-weight:900;font-size:17.5px;line-height:38px;text-align:center;text-transform:uppercase}

.signoff{left:24px;top:880px;font-family:'Yellowtail',cursive;font-size:30px;line-height:38px;color:var(--ink)}
.team{left:24px;top:922px;font-size:20px;font-weight:900;text-transform:uppercase}
.team span{color:var(--red)}

.phone-bar{left:559px;top:884px;width:339px;height:60px}
.phone-icon{left:576px;top:894px}
.phone-number{right:32px;top:886px;font-family:'Oswald',sans-serif;font-weight:700;font-size:42px;line-height:56px;color:#fff;white-space:nowrap}

/* bottom row */
.urgency{left:26px;top:972px;width:352px;height:130px;background:var(--navy);padding:18px 0 0 18px;color:#fff;font-family:'Oswald',sans-serif;text-transform:uppercase}
.urgency h2{font-size:30px;font-weight:700;line-height:36px}
.urgency p{font-size:19px;font-weight:500;line-height:23px;margin-top:6px;color:#e6e8ee}

.feature{top:972px;width:159px;height:130px;border:3px solid var(--red);background:#fff;display:flex;flex-direction:column;align-items:center;justify-content:flex-end;padding-bottom:10px;text-align:center;font-family:'Oswald',sans-serif;font-weight:600;text-transform:uppercase;color:var(--ink);line-height:19px}
.feature svg{margin-bottom:auto;margin-top:12px}
.f1{left:395px;font-size:16.5px}
.f2{left:567px;font-size:15px}
.f3{left:739px;font-size:16.5px}

/* footer */
.footer-line{left:0;top:1114px;width:922px;height:5px;background:var(--red)}
.footer-cta{left:0;top:1114px;width:560px;height:86px}
.footer-cta-text{left:24px;top:1135px;font-family:'Oswald',sans-serif;font-weight:700;font-size:36px;line-height:44px;color:#fff;text-transform:uppercase}
.partners{left:512px;top:1150px;width:384px;display:flex;justify-content:space-between;align-items:center;font-family:'Lato',sans-serif;font-weight:900;font-size:17px}
.p-quinta{color:var(--navy);font-size:14px}
.p-borvo{color:var(--ink)}
.p-kwm{color:var(--red)}
.p-velimar{color:var(--sun)}
</style>
</head>
<body>
<main class="email">

  <svg class="abs hero-photo" viewBox="0 0 922 440" role="img" aria-label="Photo of a modern home with rooftop solar panels and wall-mounted battery units at sunset">
    <defs>
      <linearGradient id="heroGrad" x1="0" y1="0" x2="1" y2="1">
        <stop offset="0" stop-color="#f6c36a"/>
        <stop offset=".35" stop-color="#c98a45"/>
        <stop offset=".7" stop-color="#6f7a63"/>
        <stop offset="1" stop-color="#8c8f8a"/>
      </linearGradient>
    </defs>
    <polygon points="380,140 922,140 922,440 440,440" fill="url(#heroGrad)"/>
  </svg>

  <svg class="abs headline-band" viewBox="0 0 922 150" aria-hidden="true">
    <polygon points="420,0 922,0 922,150 370,150" fill="var(--red)"/>
  </svg>
  <h1 class="abs headline">National Cell<br>Storage Grant</h1>
  <div class="abs headline-script">is coming!</div>

  <div class="abs brand">
    <div class="brand-square"></div>
    <div class="brand-name">Tamsel Energy</div>
  </div>
  <div class="abs brand-tag">Engineering and Economic Solutions</div>
  <div class="abs brand-reg">ABN: 41 902 357 118<br>Electrical Contractors Number: 63048</div>

  <svg class="abs web-bar" viewBox="0 0 360 40" aria-hidden="true">
    <polygon points="0,0 348,0 360,40 0,40" fill="var(--red)"/>
  </svg>
  <div class="abs web-text">www.tamselenergy.com.au</div>

  <svg class="abs hero-box" viewBox="0 0 440 128" aria-hidden="true">
    <polygon points="0,0 400,0 440,128 0,128" fill="var(--navy)"/>
  </svg>
  <h2 class="abs hero-title">Maximise your<br>solar savings</h2>

  <div class="abs greet-band"></div>
  <p class="abs greet">Hi [First Name]</p>

  <p class="abs lead"><em>Great news!</em> With the federal election now decided,<br>the National Household Cell Grant Initiative is officially on the way.</p>
  <p class="abs para">While the scheme hasn’t formally launched yet, it’s guaranteed—and like the solar rebate before it, the subsidy reduces each year, so the earlier you install, the more you’ll save. Crucially, the subsidy is only available once per household, so it makes sense to install a system that fully meets your home’s battery needs right from the start.</p>

  <svg class="abs why-bar" viewBox="0 0 594 33" aria-hidden="true">
    <defs>
      <linearGradient id="whyGrad" x1="0" x2="1">
        <stop offset="0" stop-color="var(--navy)"/>
        <stop offset=".55" stop-color="#5a2c3c"/>
        <stop offset="1" stop-color="var(--red)"/>
      </linearGradient>
    </defs>
    <polygon points="0,0 580,0 594,33 0,33" fill="url(#whyGrad)"/>
  </svg>
  <h3 class="abs why-text">Why add a battery to your existing solar system now?</h3>

  <ul class="abs benefits">
    <li><svg class="bullet" viewBox="0 0 20 14" aria-hidden="true"><rect width="20" height="14" fill="var(--red)"/><path d="M0 5H20M0 9.5H20M7 0V14M13.5 0V14" stroke="#fff" stroke-width="1"/></svg><span><b>Store your excess solar energy</b> instead of sending it back to the grid for low feed-in tariffs</span></li>
    <li><svg class="bullet" viewBox="0 0 20 14" aria-hidden="true"><rect width="20" height="14" fill="var(--red)"/><path d="M0 5H20M0 9.5H20M7 0V14M13.5 0V14" stroke="#fff" stroke-width="1"/></svg><span><b>Use your stored solar power at night,</b> when electricity prices are highest (typically 5–8pm)</span></li>
    <li><svg class="bullet" viewBox="0 0 20 14" aria-hidden="true"><rect width="20" height="14" fill="var(--red)"/><path d="M0 5H20M0 9.5H20M7 0V14M13.5 0V14" stroke="#fff" stroke-width="1"/></svg><span><b>Slash your power bills</b> and avoid rising time-of-use charges</span></li>
    <li><svg class="bullet" viewBox="0 0 20 14" aria-hidden="true"><rect width="20" height="14" fill="var(--red)"/><path d="M0 5H20M0 9.5H20M7 0V14M13.5 0V14" stroke="#fff" stroke-width="1"/></svg><span><b>Protect your home</b> from power outages</span></li>
    <li><svg class="bullet" viewBox="0 0 20 14" aria-hidden="true"><rect width="20" height="14" fill="var(--red)"/><path d="M0 5H20M0 9.5H20M7 0V14M13.5 0V14" stroke="#fff" stroke-width="1"/></svg><span><b>Increase your self-sufficiency</b> and long-term energy security</span></li>
  </ul>

  <div class="abs note">If you’ve already installed solar with us, now is the ideal time to complete your setup with<br>a battery system designed to maximise your return—and take full advantage of this one-off federal subsidy.</div>

  <svg class="abs battery-photo" viewBox="0 0 90 242" role="img" aria-label="Product photo of a white stacked home battery unit">
    <defs>
      <linearGradient id="batGrad" x1="0" x2="1">
        <stop offset="0" stop-color="#d9dbe0"/>
        <stop offset=".5" stop-color="#f4f5f7"/>
        <stop offset="1" stop-color="#c9ccd2"/>
      </linearGradient>
    </defs>
    <rect x="2" y="0" width="86" height="242" rx="4" fill="url(#batGrad)"/>
  </svg>

  <div class="abs cta-bar">Call us today or reply to this email to secure your spot and beat the rush!</div>

  <p class="abs signoff">Let your solar work smarter for your home</p>
  <p class="abs team">The <span>Tamsel Energy</span> Team</p>

  <svg class="abs phone-bar" viewBox="0 0 339 60" aria-hidden="true">
    <polygon points="14,0 339,0 339,60 0,60" fill="var(--red)"/>
  </svg>
  <svg class="abs phone-icon" width="40" height="40" viewBox="0 0 40 40" aria-hidden="true">
    <circle cx="20" cy="20" r="18" fill="#fff" stroke="var(--navy)" stroke-width="2"/>
    <path d="M13 11c2-1 3 0 4 2l1 3c0 1-1 2-2 2 1 3 3 5 6 6 0-1 1-2 2-2l3 1c2 1 3 2 2 4-1 2-3 3-5 2-6-2-10-6-12-12-1-2 0-4 1-6z" fill="var(--navy)"/>
  </svg>
  <div class="abs phone-number">07 3000 4815</div>

  <div class="abs urgency">
    <h2>Install a battery now!</h2>
    <p>Subsidy winds down each year,<br>limited to one per household</p>
  </div>

  <div class="abs feature f1">
    <svg width="64" height="64" viewBox="0 0 64 64" aria-hidden="true">
      <path d="M32 6a26 26 0 1 0 26 26" fill="none" stroke="var(--red)" stroke-width="5"/>
      <path d="M24 20v10M40 20v10M20 30h24v6a12 12 0 0 1-24 0z" fill="none" stroke="var(--navy)" stroke-width="4"/>
      <path d="M32 48v8" stroke="var(--navy)" stroke-width="4"/>
    </svg>
    Energy savings
  </div>
  <div class="abs feature f2">
    <svg width="60" height="60" viewBox="0 0 60 60" aria-hidden="true">
      <circle cx="30" cy="30" r="25" fill="none" stroke="var(--red)" stroke-width="5"/>
      <path d="M30 15v16h11" fill="none" stroke="var(--navy)" stroke-width="5" stroke-linecap="round"/>
    </svg>
    Time-of-use<br>charge avoidance
  </div>
  <div class="abs feature f3">
    <svg width="76" height="60" viewBox="0 0 76 60" aria-hidden="true">
      <rect x="12" y="4" width="14" height="8" fill="var(--red)"/>
      <rect x="50" y="4" width="14" height="8" fill="var(--red)"/>
      <rect x="2" y="12" width="72" height="44" rx="3" fill="var(--navy)"/>
      <path d="M12 26h10M17 21v10M54 26h10" stroke="#fff" stroke-width="3"/>
      <path d="M40 20l-7 14h6l-3 12 9-16h-6z" fill="var(--red)"/>
    </svg>
    Self-sufficiency
  </div>

  <div class="abs footer-line"></div>
  <svg class="abs footer-cta" viewBox="0 0 560 86" aria-hidden="true">
    <polygon points="0,0 510,0 470,86 0,86" fill="var(--red)"/>
  </svg>
  <a class="abs footer-cta-text">Secure my battery now</a>
  <div class="abs partners">
    <span class="p-quinta">QuintaPWR</span>
    <span class="p-borvo">BORVO</span>
    <span class="p-kwm">KWM</span>
    <span class="p-velimar">VELIMAR</span>
  </div>

</main>
</body>
</html>
```